Oil and Gas Exploration and Production company needs a business card design

We need a business card design using our logo and colors in the logo. We want a mainstream design.

```html
<!DOCTYPE html>
<html lang="en">
<head>
<meta charset="utf-8">
<title>Solcrest Energy – Business Card</title>
<link href="https://fonts.googleapis.com/css2?family=Open+Sans:wght@400;600;700&family=Roboto+Condensed:wght@300&display=swap" rel="stylesheet">
<style>
  :root {
    --gold: #b07d1c;
    --gold-deep: #9a6b12;
    --paper: #f2f2f1;
    --ink: #141414;
    --backdrop: #e4e4e4;
  }
  * { box-sizing: border-box; margin: 0; padding: 0; }
  html, body {
    width: 1200px; height: 1200px; overflow: hidden;
    background: var(--backdrop);
  }
  .sheet {
    width: 1200px; height: 1200px;
    display: flex; flex-direction: column; align-items: center; justify-content: center;
    gap: 64px;
  }
  .card {
    position: relative;
    width: 840px; height: 480px;
    background: var(--paper);
    box-shadow: 0 10px 30px rgba(0,0,0,0.12);
    overflow: hidden;
    font-family: "Open Sans", sans-serif;
    color: var(--ink);
  }
  .card-shape { position: absolute; inset: 0; }
  .brand {
    position: absolute;
    display: flex; align-items: center; gap: 14px;
    font-family: "Open Sans", sans-serif;
    font-weight: 700; color: var(--ink);
    letter-spacing: -0.5px;
    white-space: nowrap;
  }
  .brand-dot {
    width: 40px; height: 40px; border-radius: 50%;
    background: var(--ink); flex: none;
  }
  .card-front .brand { left: 215px; top: 72px; font-size: 46px; }
  .card-back .brand { left: 50%; top: 50%; transform: translate(-50%, -50%); font-size: 62px; }
  .card-back .brand-dot { width: 52px; height: 52px; }
  .holder {
    position: absolute; left: 180px; top: 196px; width: 248px;
    text-align: right;
  }
  .holder-name {
    font-family: "Roboto Condensed", sans-serif; font-weight: 300;
    font-size: 34px; color: var(--gold); letter-spacing: -0.5px;
  }
  .holder-role { font-size: 17px; font-weight: 600; margin-top: -2px; }
  .contact {
    position: absolute; left: 440px; top: 250px;
    border-left: 2px solid var(--gold);
    padding-left: 14px;
    font-size: 16px; font-weight: 600; line-height: 28px;
    white-space: nowrap;
  }
  .contact-address-block { top: 350px; }
  .contact-row { display: flex; align-items: center; gap: 8px; }
  .contact-row svg { width: 16px; height: 16px; flex: none; fill: var(--gold-deep); }
  .accent { color: var(--gold); }
  .contact-address { padding-left: 24px; }
</style>
</head>
<body>
<main class="sheet">
  <section class="card card-front" aria-label="Business card front">
    <svg class="card-shape" viewBox="0 0 840 480" aria-hidden="true">
      <rect width="840" height="480" fill="var(--gold)"/>
      <ellipse cx="440" cy="240" rx="344" ry="414" fill="none" stroke="#f2f2f1" stroke-width="3"/>
      <ellipse cx="440" cy="240" rx="330" ry="400" fill="var(--paper)"/>
    </svg>

    <div class="brand"><span class="brand-dot"></span>Solcrest Energy</div>

    <div class="holder">
      <p class="holder-name">JOHN DOE</p>
      <p class="holder-role">Director</p>
    </div>

    <div class="contact">
      <p class="contact-row">
        <svg viewBox="0 0 16 16"><path d="M3 2h3l1.5 3.5-2 1.2a8 8 0 0 0 3.8 3.8l1.2-2L14 10v3a1 1 0 0 1-1 1A11 11 0 0 1 2 3a1 1 0 0 1 1-1z"/></svg>
        <span>1-234-567890</span>
      </p>
      <p class="contact-row">
        <svg viewBox="0 0 16 16"><path d="M1 3h14v10H1z M1 3l7 6 7-6" stroke="#f2f2f1" stroke-width="1"/></svg>
        <span>john@<span class="accent">solcrestenergy</span>.com</span>
      </p>
      <p class="contact-row">
        <svg viewBox="0 0 16 16"><circle cx="8" cy="8" r="6.5" fill="none" stroke="var(--gold-deep)" stroke-width="1.4"/><path d="M1.5 8h13M8 1.5c-3 3.5-3 9.5 0 13M8 1.5c3 3.5 3 9.5 0 13" fill="none" stroke="var(--gold-deep)" stroke-width="1.2"/></svg>
        <span>www.<span class="accent">solcrestenergy</span>.com</span>
      </p>
    </div>
    <div class="contact contact-address-block">
      <p class="contact-row">
        <svg viewBox="0 0 16 16"><path d="M8 1a5 5 0 0 1 5 5c0 4-5 9-5 9S3 10 3 6a5 5 0 0 1 5-5zm0 3a2 2 0 1 0 0 4 2 2 0 0 0 0-4z"/></svg>
        <span>Dummy city</span>
      </p>
      <p class="contact-address">Dummy Country Land</p>
    </div>
  </section>

  <section class="card card-back" aria-label="Business card back">
    <div class="brand"><span class="brand-dot"></span>Solcrest Energy</div>
  </section>
</main>
</body>
</html>
```